FOOD DELIVERY BRAND NEEDS WEBSITE TO GET SUBSCRIBERS

web design needed for a food delivery brand/label,
website should display who we are, how it works and push futur clients to get the label for an online application. Should look serious/official, trustworthy and confident. colors are black and gold like logo

Target Market(s)

restaurants

Industry/Entity Type

restaurant

Number of Pages Required

4 page

Requirements
Must have
• home page, who we are, our partners, subscribe, 2 subscribe button : 1 on top 1 bottom
Nice to have
• a graphic showing average + 15% sales thanks the label

```html
<!DOCTYPE html>
<html lang="en">
<head>
<meta charset="utf-8">
<title>Aurum Plate Seal</title>
<link href="https://fonts.googleapis.com/css2?family=Libre+Baskerville:wght@700&family=Open+Sans:ital,wght@0,400;0,600;0,700;1,400&family=Montserrat:wght@600;700&display=swap" rel="stylesheet">
<style>
:root{
  --gold:#c9a04a;
  --gold-dark:#a98532;
  --black:#0d0d0d;
  --ink:#222;
  --grey-band:#cfcfcf;
  --grey-dark:#575757;
  --hero-bg:#ececec;
  --white:#fff;
}
*{box-sizing:border-box;margin:0;padding:0}
html,body{width:1200px;height:2936px;overflow:hidden}
body{position:relative;background:var(--white);font-family:"Open Sans",sans-serif;color:var(--ink)}
.abs{position:absolute}
.shapes{position:absolute;left:0;top:0;width:1200px;height:2936px}
.serif{font-family:"Libre Baskerville",serif;font-weight:700}

/* header */
.site-header{left:0;top:0;width:1200px;height:93px;background:var(--black)}
.brand{left:200px;top:22px;width:110px;text-align:center;color:var(--gold);font-family:"Montserrat",sans-serif;font-weight:700;font-size:12px;line-height:14px;letter-spacing:.5px}
.brand .mark{display:block;width:26px;height:26px;border-radius:50%;background:var(--gold);margin:0 auto 6px}
.brand-divider{left:180px;top:0;width:1px;height:93px;background:#222}
.nav{top:42px;font-family:"Montserrat",sans-serif;font-size:9.5px;font-weight:600;color:var(--white);letter-spacing:.3px}
.nav.active{color:var(--gold)}
.btn{display:flex;align-items:center;justify-content:center;font-family:"Montserrat",sans-serif;font-weight:700;font-size:9.5px;letter-spacing:.4px}
.btn-solid{background:var(--gold);color:var(--black)}
.btn-outline{border:2px solid var(--gold);color:var(--gold)}
.subscribe-top{left:887px;top:28px;width:112px;height:37px}

/* hero */
.hero-title{left:200px;top:190px;width:400px;font-size:33px;line-height:45px;color:#111}
.call-now{left:200px;top:387px;width:113px;height:37px}
.badge{left:744px;top:463px;width:118px;height:118px;border-radius:50%;background:var(--gold);border:4px solid var(--white);box-shadow:0 0 0 2px var(--gold)}
.badge-inner{position:absolute;inset:7px;border:1.5px dashed #5a4514;border-radius:50%;display:flex;flex-direction:column;align-items:center;justify-content:center;color:#2b210a;font-family:"Montserrat",sans-serif;font-weight:600}
.badge-inner small{font-size:10px;letter-spacing:.5px}
.badge-inner b{font-size:28px;color:var(--white);line-height:34px;font-weight:600}

/* how it works */
.section-title{width:1200px;left:0;text-align:center;font-size:25px;color:#111}
.step-icon{width:68px;height:68px;border-radius:50%;border:1.5px dashed var(--gold);display:flex;align-items:center;justify-content:center}
.step-text{width:160px;text-align:center;font-size:12.5px;line-height:15px;color:#222}

/* welcome */
.welcome-kicker{left:0;width:1200px;top:1077px;text-align:center;color:var(--white);font-weight:600;font-size:15px}
.welcome-title{left:0;width:1200px;top:1106px;text-align:center;color:var(--gold);font-size:33px}
.welcome-copy{left:200px;width:800px;text-align:center;color:var(--white);font-size:9.5px;line-height:15px}
.contact-btn{left:538px;top:1277px;width:124px;height:37px;background:transparent}

/* testimonials */
.card{width:388px;height:187px;background:#f4f4f4;box-shadow:0 2px 6px rgba(0,0,0,.08);padding:26px 26px 0}
.card h4{font-weight:400;font-size:13.5px;color:#222;margin-bottom:14px}
.card p{font-style:italic;font-size:12.5px;line-height:19px;color:#333}
.card .stars{color:var(--gold);font-size:12px;letter-spacing:1px;margin-top:12px}
.card::after{content:"";position:absolute;left:38px;bottom:-10px;border:10px solid transparent;border-bottom:0;border-top-color:#f4f4f4}
.avatar{width:38px;height:38px;border-radius:50%;background:var(--gold);color:var(--white);display:flex;align-items:center;justify-content:center;font-weight:700;font-size:14px}
.client-name{font-size:10.5px;color:#222}
.arrow-nav{font-size:14px;color:#222}
.view-all{left:550px;top:1773px;width:100px;height:37px;border:2px solid var(--gold-dark);color:#333;background:transparent}

/* partners */
.partner{width:150px;height:83px;background:var(--white);box-shadow:0 2px 8px rgba(0,0,0,.09);display:flex;align-items:center;justify-content:center}
.partner span{display:block;width:58px;height:58px;border-radius:50%;background:#e9e3d3}
.dot{width:10px;height:10px;border-radius:50%;border:1.5px solid var(--gold);top:2174px}
.dot.on{background:radial-gradient(var(--gold) 35%,transparent 40%)}

/* newsletter */
.news-kicker{left:0;width:1200px;top:2385px;text-align:center;color:var(--white);font-weight:600;font-size:15px}
.news-title{left:0;width:1200px;top:2416px;text-align:center;color:var(--gold);font-size:32px}
.news-sub{left:0;width:1200px;top:2457px;text-align:center;color:var(--white);font-size:15px}
.news-form{left:322px;top:2498px;width:556px;height:37px;border:2px solid var(--white);display:flex}
.news-form .field{flex:1;color:var(--white);font-size:10px;padding-left:16px;display:flex;align-items:center}
.news-form .btn{width:112px;margin:-2px -2px -2px 0;height:37px}

/* footer */
.site-footer{left:0;top:2599px;width:1200px;height:337px;background:var(--black)}
.foot-brand{left:200px;top:2665px;width:150px;text-align:center;color:var(--gold);font-family:"Montserrat",sans-serif;font-weight:700;font-size:15px;line-height:17px}
.foot-brand .mark{display:block;width:44px;height:44px;border-radius:50%;background:var(--gold);margin:0 auto 12px}
.foot-head{color:var(--gold);font-weight:600;font-size:13.5px}
.foot-line{color:var(--white);font-size:11px;display:flex;align-items:flex-start;gap:12px;line-height:15px}
.foot-line.big{font-size:15px}
.foot-link{color:var(--white);font-size:9.5px}
.social{left:969px;width:32px;height:32px;border-radius:50%;background:#3a3a3a}
.social.on{background:var(--gold)}
.copyright{left:200px;top:2868px;color:var(--white);font-size:9px}
.copyright em{color:var(--gold);font-style:normal}
</style>
</head>
<body>

<svg class="shapes" viewBox="0 0 1200 2936" aria-hidden="true">
  <polygon points="0,93 1200,93 1200,450 302,615 0,456" fill="var(--hero-bg)"/>
  <polygon points="51,490 302,650 1048,490 302,625" fill="var(--gold)"/>
  <polygon points="148,1077 898,917 1145,1077 898,958" fill="var(--gold)"/>
  <polygon points="0,1111 898,974 1200,1111 1200,1380 0,1380" fill="#2a2a2a"/>
  <polygon points="0,1380 1200,1380 1200,1766 302,1926 0,1766" fill="var(--grey-band)"/>
  <polygon points="51,1800 302,1960 1048,1800 302,1932" fill="var(--gold)"/>
  <polygon points="148,2399 898,2243 1145,2399 898,2282" fill="var(--gold)"/>
  <polygon points="0,2433 898,2277 1200,2433 1200,2599 0,2599" fill="var(--grey-dark)"/>
  <path d="M203,725 C240,745 250,770 280,778 S400,795 440,789 S560,760 600,756 S720,789 760,789 S880,770 920,756 S980,735 997,725" fill="none" stroke="var(--gold)" stroke-width="1.2" stroke-dasharray="3 3"/>
  <circle cx="203" cy="725" r="3" fill="var(--gold)"/>
  <circle cx="997" cy="725" r="3" fill="var(--gold)"/>
</svg>

<svg class="abs" style="left:560px;top:93px" width="640" height="430" viewBox="0 0 640 430" role="img" aria-label="Plated grilled steak with vegetables, fruit and a pepper mill on a light table">
  <defs>
    <linearGradient id="heroPhoto" x1="0" y1="0" x2="1" y2="1">
      <stop offset="0" stop-color="#eadfdf"/>
      <stop offset=".5" stop-color="#a86a4a"/>
      <stop offset="1" stop-color="#5a3a28"/>
    </linearGradient>
  </defs>
  <polygon points="120,0 640,0 640,360 240,430 60,300" fill="url(#heroPhoto)" opacity=".85"/>
</svg>

<svg class="abs" style="left:0;top:917px" width="1200" height="463" viewBox="0 0 1200 463" role="img" aria-label="Person ordering food delivery on a laptop, dark toned">
  <defs>
    <linearGradient id="welcomePhoto" x1="0" y1="0" x2="1" y2="0">
      <stop offset="0" stop-color="#3b342e"/>
      <stop offset=".6" stop-color="#2b2622"/>
      <stop offset="1" stop-color="#1c1a19"/>
    </linearGradient>
  </defs>
  <polygon points="0,194 898,57 1200,194 1200,463 0,463" fill="url(#welcomePhoto)"/>
</svg>

<header class="abs site-header"></header>
<div class="abs brand-divider"></div>
<div class="abs brand"><span class="mark"></span>AURUM PLATE<br>SEAL</div>
<div class="abs nav active" style="left:626px">- HOME -</div>
<div class="abs nav" style="left:696px">WHO WE ARE</div>
<div class="abs nav" style="left:785px">OUR PARTNERS</div>
<div class="abs btn btn-solid subscribe-top">SUBSCRIBE NOW!</div>

<h1 class="abs hero-title serif">Lorem Ipsum is simply dummy text of the printing and typesetting.</h1>
<div class="abs btn btn-solid call-now">CALL NOW!</div>
<div class="abs badge"><div class="badge-inner"><small>AVERAGE</small><b>+ 15%</b><small>SALES</small></div></div>

<h2 class="abs section-title serif" style="top:664px">How it works</h2>

<div class="abs step-icon" style="left:246px;top:722px"><svg width="30" height="26" viewBox="0 0 30 26" fill="none" stroke="var(--gold)" stroke-width="1.8"><path d="M3 11a12 9 0 0 1 24 0z"/><rect x="2" y="13" width="26" height="4" rx="1"/><path d="M3 20h24v2a2 2 0 0 1-2 2H5a2 2 0 0 1-2-2z"/></svg></div>
<div class="abs step-text" style="left:200px;top:805px">Open the Aurum Plate and select "Food"</div>

<div class="abs step-icon" style="left:406px;top:755px"><svg width="24" height="32" viewBox="0 0 24 32" fill="none" stroke="var(--gold)" stroke-width="1.8"><path d="M12 30S2 18 2 11a10 10 0 0 1 20 0c0 7-10 19-10 19z"/><circle cx="12" cy="11" r="4"/></svg></div>
<div class="abs step-text" style="left:360px;top:837px">Enter your delivery address.</div>

<div class="abs step-icon" style="left:566px;top:722px"><svg width="28" height="32" viewBox="0 0 28 32" fill="none" stroke="var(--gold)" stroke-width="1.8"><ellipse cx="7" cy="9" rx="5" ry="7"/><path d="M7 16v14"/><path d="M17 2v9a4 4 0 0 0 8 0V2M21 2v28"/></svg></div>
<div class="abs step-text" style="left:520px;top:805px">Select your favourite restaurant.</div>

<div class="abs step-icon" style="left:726px;top:755px"><svg width="32" height="28" viewBox="0 0 32 28" fill="none" stroke="var(--gold)" stroke-width="1.8"><path d="M2 11h28l-4 15H6z"/><path d="M9 11l7-9 7 9M12 15v7M16 15v7M20 15v7"/></svg></div>
<div class="abs step-text" style="left:680px;top:837px">Select a food and add to your basket.</div>

<div class="abs step-icon" style="left:886px;top:722px"><svg width="36" height="20" viewBox="0 0 36 20" fill="none" stroke="var(--gold)" stroke-width="1.8"><path d="M2 10l7 7L24 2M14 15l2 2L34 2"/></svg></div>
<div class="abs step-text" style="left:840px;top:805px">Complete the order and get ready to enjoy your food.</div>

<div class="abs welcome-kicker">Welcome to</div>
<h2 class="abs welcome-title serif">Aurum Plate Seal</h2>
<p class="abs welcome-copy" style="top:1161px">It is a long established fact that a reader will be distracted by the readable content of a page when looking at its layout. The point of using Lorem Ipsum is that it has a more-or-less normal distribution of letters, as opposed to using 'Content here, content here', making it look like readable English. Many desktop publishing packages and web page editors now use Lorem Ipsum as their default model text, and a search for 'lorem ipsum' will uncover many web sites still in their infancy.</p>
<p class="abs welcome-copy" style="top:1221px">Contrary to popular belief, Lorem Ipsum is not simply random text. It has roots in a piece of classical Latin literature from 45 BC, making it over 2000 years old. Dorian Vellmont, a Latin professor at Castor Vale College in Lorem, looked up one of the more obscure Latin words, consectetur,</p>
<div class="abs btn btn-outline contact-btn">CONTACT US TODAY!</div>

<h2 class="abs section-title serif" style="top:1440px">Happy Clients Say</h2>
<div class="abs arrow-nav" style="left:149px;top:1585px">&#8249;</div>
<div class="abs arrow-nav" style="left:1043px;top:1585px">&#8250;</div>

<div class="abs card" style="left:199px;top:1496px">
  <h4>Aurum Plate Seal</h4>
  <p>It is a long established fact that a reader will be distracted by the readable content of a page when looking at its layout. The point of using Lorem Ipsum is that it has a more-or-less normal distribution of letters, as opposed to using 'Content here, content here ...</p>
  <div class="stars">★★★★★</div>
</div>
<div class="abs avatar" style="left:225px;top:1705px">S</div>
<div class="abs client-name" style="left:277px;top:1718px">Standard Chunk</div>

<div class="abs card" style="left:612px;top:1496px">
  <h4>Aurum Plate Seal</h4>
  <p>It is a long established fact that a reader will be distracted by the readable content of a page when looking at its layout. The point of using Lorem Ipsum is that it has a more-or-less normal distribution of letters, as opposed to using 'Content here, content here ...</p>
  <div class="stars">★★★★★</div>
</div>
<div class="abs avatar" style="left:638px;top:1705px">S</div>
<div class="abs client-name" style="left:690px;top:1718px">Standard Chunk</div>

<div class="abs btn view-all">VIEW ALL</div>

<h2 class="abs section-title serif" style="top:2005px">Our partners</h2>
<div class="abs partner" style="left:199px;top:2060px"><span></span></div>
<div class="abs partner" style="left:361px;top:2060px"><span></span></div>
<div class="abs partner" style="left:524px;top:2060px"><span></span></div>
<div class="abs partner" style="left:686px;top:2060px"><span></span></div>
<div class="abs partner" style="left:849px;top:2060px"><span></span></div>
<div class="abs dot" style="left:562px"></div>
<div class="abs dot on" style="left:583px"></div>
<div class="abs dot" style="left:603px"></div>
<div class="abs dot" style="left:624px"></div>

<div class="abs news-kicker">Subscribe Now</div>
<h2 class="abs news-title serif">Sign Up Newletter</h2>
<div class="abs news-sub">Newsletter promo sign up receive 10%off first purchase</div>
<div class="abs news-form"><div class="field">Enter Your Email ...</div><div class="btn btn-solid">SUBSCRIBE</div></div>

<footer class="abs site-footer"></footer>
<div class="abs foot-brand"><span class="mark"></span>AURUM PLATE<br>SEAL</div>

<div class="abs foot-head" style="left:425px;top:2663px">Contact Info</div>
<div class="abs foot-line big" style="left:425px;top:2692px"><svg width="12" height="12" viewBox="0 0 12 12" fill="var(--gold)"><path d="M2 1l2 0 1 3-1.5 1a7 7 0 0 0 3.5 3.5L8 7l3 1v2a1 1 0 0 1-1 1A9 9 0 0 1 1 2a1 1 0 0 1 1-1z"/></svg>123-456-7890</div>
<div class="abs foot-line" style="left:425px;top:2727px"><svg width="12" height="10" viewBox="0 0 12 10" fill="var(--gold)"><path d="M0 1h12v8H0z"/><path d="M0 1l6 4 6-4" stroke="#0d0d0d" fill="none"/></svg>info@aurumplate.com</div>
<div class="abs foot-line" style="left:425px;top:2757px"><svg width="10" height="13" viewBox="0 0 10 13" fill="var(--gold)"><path d="M5 13S0 7 0 5a5 5 0 0 1 10 0c0 2-5 8-5 8z"/></svg><span>Lorem House Level 3, 1500<br>Ipsum St Lorem - 6011</span></div>

<div class="abs foot-head" style="left:701px;top:2663px">Quick Links</div>
<div class="abs foot-link" style="left:701px;top:2696px">Home</div>
<div class="abs foot-link" style="left:701px;top:2719px">Who We Are</div>
<div class="abs foot-link" style="left:701px;top:2742px">Our Partners</div>
<div class="abs foot-link" style="left:701px;top:2764px">Testimonials</div>
<div class="abs foot-link" style="left:701px;top:2787px">Contact Us</div>
<div class="abs foot-link" style="left:791px;top:2696px">Terms and Conditions</div>
<div class="abs foot-link" style="left:791px;top:2719px">Privacy Notice</div>

<div class="abs social" style="top:2664px"></div>
<div class="abs social on" style="top:2702px"></div>
<div class="abs social" style="top:2740px"></div>

<div class="abs copyright">© 2022 <em>Aurum Plate Seal</em>. All Right Reserved</div>
<svg class="abs" style="left:1093px;top:2863px" width="16" height="18" viewBox="0 0 16 18" aria-hidden="true"><path d="M8 0l8 18-8-5-8 5z" fill="var(--gold)"/></svg>

</body>
</html>
```